Consulting firm business card, email signature, stationery
Halverton Advisory Group
Use standard fonts
Same font or standard is fine
Peter L. Dravik
President
842 S. Tolliver Street
Clayton, MO 63105
pete.dravik@halvertonag.example
halvertonag.example
The font can be standard for a professional consulting firm, or you can try with matching the logo.
The business card and email signature are most important. Stationery would be a nice bonus.
Ai version of logo file

```html
<!DOCTYPE html>
<html lang="en">
<head>
<meta charset="utf-8">
<title>Halverton Advisory Group – Business Card</title>
<link href="https://fonts.googleapis.com/css2?family=Cinzel:wght@400;600&display=swap" rel="stylesheet">
<style>
  :root {
    --backdrop: #d9d9d9;
    --paper: #ffffff;
    --paper-edge: #e6e8ec;
    --navy: #1d3f8f;
    --navy-deep: #0f2461;
    --navy-light: #3a63c4;
    --ink: #2b2b2b;
    --ink-soft: #6a6a6a;
    --accent: #ef7d1a;
    --white: #ffffff;
  }
  * { margin: 0; padding: 0; box-sizing: border-box; }
  html, body {
    width: 1200px; height: 901px; overflow: hidden;
    background: var(--backdrop);
    font-family: "Cinzel", "Times New Roman", serif;
  }
  .sheet {
    width: 1200px; height: 901px;
    display: flex; align-items: center; justify-content: center; gap: 60px;
  }
  .card {
    width: 500px; height: 286px; position: relative; overflow: hidden;
    box-shadow: 0 10px 28px rgba(0,0,0,.18);
  }
  /* Front */
  .card-front { background: var(--paper); border: 1px solid var(--paper-edge); }
  .brand { position: absolute; left: 34px; top: 30px; display: flex; align-items: center; gap: 12px; }
  .brand-dot { width: 30px; height: 30px; border-radius: 50%; background: var(--navy); }
  .brand-name { color: var(--navy); font-weight: 600; font-size: 19px; line-height: 1.05; letter-spacing: .5px; max-width: 230px; }
  .contact { position: absolute; left: 96px; top: 112px; color: var(--ink); }
  .person-name { font-size: 15px; font-weight: 600; letter-spacing: .5px; }
  .person-title { font-size: 9px; color: var(--ink-soft); letter-spacing: 1px; margin-top: 2px; }
  .address { font-size: 8.5px; line-height: 1.45; margin-top: 12px; color: var(--ink-soft); }
  .lines { list-style: none; margin-top: 8px; font-size: 8.5px; line-height: 1.55; color: var(--ink-soft); }
  .lines li { display: flex; align-items: center; gap: 5px; }
  .lines li::before { content: ""; width: 4px; height: 4px; background: var(--accent); display: inline-block; }
  .footer-band {
    position: absolute; left: 0; right: 0; bottom: 0; height: 26px;
    background: linear-gradient(90deg, var(--navy-deep), var(--navy));
    display: flex; align-items: center; padding-left: 34px;
    color: var(--white); font-size: 8px; letter-spacing: 1.5px;
  }
  .footer-dot { position: absolute; right: 18px; bottom: 32px; width: 22px; height: 22px; border-radius: 50%; background: var(--navy); }
  /* Back */
  .card-back {
    background: radial-gradient(circle at 50% 42%, var(--navy-light) 0%, var(--navy) 45%, var(--navy-deep) 100%);
    display: flex; flex-direction: column; align-items: center; justify-content: center; gap: 14px;
  }
  .back-name { color: var(--white); font-weight: 600; font-size: 20px; letter-spacing: 1px; text-align: center; line-height: 1.1; }
  .back-site { color: var(--white); font-size: 9px; letter-spacing: 3px; opacity: .85; }
</style>
</head>
<body>
<main class="sheet">
  <section class="card card-front" aria-label="Business card front">
    <div class="brand">
      <span class="brand-dot"></span>
      <span class="brand-name">Halverton Advisory Group</span>
    </div>
    <div class="contact">
      <p class="person-name">Peter L. Dravik</p>
      <p class="person-title">President</p>
      <p class="address">842 S. Tolliver Street<br>Clayton, MO 63105</p>
      <ul class="lines">
        <li>T 314.555.0142</li>
        <li>F 314.555.0178</li>
        <li>pete.dravik@halvertonag.example</li>
      </ul>
    </div>
    <span class="footer-dot"></span>
    <div class="footer-band">www.halvertonag.example</div>
  </section>

  <section class="card card-back" aria-label="Business card back">
    <p class="back-name">Halverton<br>Advisory Group</p>
    <p class="back-site">www.halvertonag.example</p>
  </section>
</main>
</body>
</html>
```